Greek delicatessen shop Signage

We have a Greek delicatessen where we have three different large windows, where on the upper side of them, we would need three different window stickers of a similar theme. I have listed below the words we would like to be written on each different window sticker with all of these stickers needing an image to be included also which I have attached and named accordingly.

1st window (Dimensions 148cm width X 50cm height)
Wording underneath the attached logo (which is named 1st window) which must go first would be the following:
Premium olive oils, large cheese selection, retsina, ready meals, olives, wine, pasta, dolmades, pita bread, baklava, taramasalata, tzatziki, spanakopita, dried herbs, vinegars, spreads, beer, jams, tomato products, fruit preserves, cookies, breadsticks, halva, salts, mastic gum, dried fruit, coffee, tea etc etc
Ideally we would like the wording to start with large letters and get smaller as we go down the list and become infinit if possible.

Second window (Dimensions 148cm width X 50cm height) which must include the image of a souvlaki wrap (attachment named 2nd window-this can be cropped accordingly )
Wording would be the following:
Authentic Greek Souvlaki
-Gyros
-Chicken
-Vegeterian
Classic size $10.00
Jumbo size $15.00
Wednesday to Sunday 10.30am to 2.30pm

Third window (Dimensions 220cm width X 50cm height)
Wording underneath the logo named 3rd window would be the following.
Private venue available for Greek cooking lessons, birthday parties, corporate lunches, catering, team building and more. Ask our friendly staff for more information or call Marta at 027359260.

Target Market(s)

retail customers

Colors
34a7d7
3176b5
add136

Requirements
Nice to have
• Nice to have a playfull feel
Should not have
• would like to avoid Greek fonts and images of Greek monuments etc

```html
<!DOCTYPE html>
<html lang="en">
<head>
<meta charset="utf-8">
<title>Greek Delicatessen Window Stickers</title>
<link rel="stylesheet" href="https://fonts.googleapis.com/css2?family=Poppins:wght@500;600;700&family=Bitter:wght@400;700&family=Noto+Serif:ital,wght@0,700;0,800;1,700&family=Lilita+One&family=Oswald:wght@400;500&display=swap">
<style>
  :root {
    --lime: #a8c422;
    --lime-deep: #94b01a;
    --olive: #5b6b1f;
    --olive-band: #5f6b2f;
    --word-grey: #8b8b8b;
    --white: #ffffff;
    --blue: #3176b5;
    --bg-dark: #363636;
    --bg-light: #7a7a7a;
  }
  * { margin: 0; padding: 0; box-sizing: border-box; }
  html, body { width: 1191px; height: 1200px; overflow: hidden; }
  body {
    position: relative;
    background: linear-gradient(120deg, var(--bg-dark) 0%, #5a5a5a 55%, var(--bg-light) 100%);
    font-family: "Bitter", serif;
  }
  .window-label {
    position: absolute; left: 0; width: 1191px; text-align: center;
    font-family: "Poppins", sans-serif; font-weight: 700; font-size: 26px;
    color: var(--white); letter-spacing: -0.3px; line-height: 1;
  }
  .sticker {
    position: absolute; background: var(--white); overflow: hidden;
    box-shadow: 4px 6px 10px rgba(0,0,0,0.45);
  }
  .sticker-frame {
    position: absolute; inset: 8px; border: 2px solid var(--lime); pointer-events: none;
  }
  /* window one */
  .sticker-products { left: 235px; top: 118px; width: 719px; height: 244px; }
  .word {
    position: absolute; color: var(--word-grey); line-height: 1; white-space: nowrap;
  }
  .word.bold { font-weight: 700; }
  .shop-mark {
    position: absolute; left: 262px; top: 62px; width: 58px; height: 58px;
    border-radius: 50%; background: var(--lime);
  }
  .shop-name {
    position: absolute; left: 236px; top: 153px; font-size: 42px; font-weight: 400;
    color: var(--olive); line-height: 1; white-space: nowrap;
  }
  .shop-tagline {
    position: absolute; left: 238px; top: 196px; font-family: "Poppins", sans-serif;
    font-weight: 500; font-size: 15px; letter-spacing: 8.6px; color: var(--lime); line-height: 1;
    white-space: nowrap;
  }
  /* window two */
  .sticker-souvlaki { left: 234px; top: 496px; width: 721px; height: 244px; }
  .souvlaki-photo {
    position: absolute; left: 0; top: 0; width: 318px; height: 244px;
    background: radial-gradient(ellipse at 60% 45%, #7a3a1c 0%, #b8743a 32%, #e7b878 58%, #f3dcb6 78%, #ffffff 100%);
  }
  .menu-title {
    position: absolute; left: 326px; font-family: "Noto Serif", serif; font-weight: 800; line-height: 1;
    white-space: nowrap;
  }
  .menu-title.lead { top: 30px; font-size: 34px; color: var(--lime); }
  .menu-title.main { top: 66px; font-size: 36px; color: var(--olive); }
  .filling-bar {
    position: absolute; left: 327px; top: 115px; width: 339px; height: 29px;
    background: var(--lime); border-radius: 3px; box-shadow: 2px 2px 0 var(--olive);
    font-family: "Noto Serif", serif; font-weight: 700; font-size: 17px; color: var(--white);
    display: flex; align-items: center; justify-content: center; letter-spacing: 0.4px;
    white-space: nowrap;
  }
  .size-tag {
    position: absolute; left: 327px; top: 164px; width: 22px; height: 51px;
    background: var(--olive); color: var(--white); font-family: "Lilita One", sans-serif;
    font-size: 13px; display: flex; align-items: center; justify-content: center;
  }
  .size-tag span { transform: rotate(-90deg); letter-spacing: 1px; }
  .size-row { position: absolute; left: 350px; height: 23px; display: flex; white-space: nowrap; }
  .size-row.classic { top: 164px; }
  .size-row.jumbo { top: 191px; }
  .size-name, .size-price {
    font-family: "Lilita One", sans-serif; font-size: 16px; line-height: 23px; letter-spacing: 0.8px;
  }
  .size-name {
    width: 78px; padding-left: 6px; color: var(--lime); background: var(--white);
    border: 1px solid var(--lime); border-right: none;
  }
  .size-price {
    width: 77px; text-align: center; color: var(--white); background: var(--lime);
    border-radius: 0 3px 3px 0;
  }
  .clock-icon { position: absolute; left: 523px; top: 173px; width: 36px; height: 36px; }
  .hours {
    position: absolute; left: 563px; font-family: "Oswald", sans-serif; color: var(--olive);
    line-height: 1; white-space: nowrap;
  }
  .hours.days { top: 172px; font-size: 14px; border-bottom: 1px solid var(--olive); padding-bottom: 3px; width: 131px; }
  .hours.time { top: 193px; font-size: 17px; font-weight: 500; }
  /* window three */
  .sticker-venue { left: 55px; top: 871px; width: 1080px; height: 246px; }
  .venue-mark {
    position: absolute; left: 78px; top: 98px; width: 24px; height: 24px; border-radius: 50%; background: var(--lime);
  }
  .venue-name {
    position: absolute; left: 110px; top: 90px; font-family: "Noto Serif", serif; font-weight: 700;
    font-size: 36px; color: var(--blue); line-height: 1; white-space: nowrap;
  }
  .venue-headline {
    position: absolute; left: 386px; top: 30px; width: 648px; text-align: center;
    font-family: "Noto Serif", serif; font-weight: 800; font-size: 51px; line-height: 1;
    color: var(--lime); text-shadow: 2px 2px 0 var(--olive); white-space: nowrap;
  }
  .venue-services {
    position: absolute; left: 386px; top: 92px; width: 648px; text-align: center;
    font-family: "Noto Serif", serif; font-style: italic; font-weight: 700; font-size: 21px;
    line-height: 26px; color: var(--olive); white-space: nowrap;
  }
  .venue-ask {
    position: absolute; left: 393px; top: 150px; width: 630px; height: 40px; border-radius: 20px;
    background: var(--olive-band); color: var(--white); font-family: "Noto Serif", serif;
    font-size: 22px; display: flex; align-items: flex-start; justify-content: center; padding-top: 4px;
    white-space: nowrap;
  }
  .venue-call {
    position: absolute; left: 491px; top: 186px; width: 433px; height: 30px; border-radius: 15px;
    background: var(--lime); display: flex; align-items: center; white-space: nowrap;
  }
  .venue-call-label {
    font-family: "Poppins", sans-serif; font-weight: 700; font-size: 21px; color: var(--white);
    padding-left: 18px; width: 240px; letter-spacing: 0.3px;
  }
  .venue-call-number {
    position: absolute; right: 0; top: 0; width: 192px; height: 30px; border-radius: 15px;
    background: var(--white); border: 1.5px solid var(--lime);
    display: flex; align-items: center; gap: 8px; padding-left: 4px;
    font-family: "Poppins", sans-serif; font-weight: 700; font-size: 21px; color: var(--olive-band);
  }
  .phone-icon { width: 23px; height: 23px; }
</style>
</head>
<body>

<div class="window-label" style="top:71px">1st window (Dimensions 148cm width X 50cm height)</div>
<section class="sticker sticker-products">
  <div class="sticker-frame"></div>
  <span class="word bold" style="left:29px;top:24px;font-size:22px">Ready meals</span>
  <span class="word" style="left:188px;top:29px;font-size:16px">Cookies</span>
  <span class="word" style="left:43px;top:56px;font-size:15px">Spreads</span>
  <span class="word" style="left:102px;top:55px;font-size:26px">Retsina</span>
  <span class="word" style="left:57px;top:83px;font-size:16px">Tomato products</span>
  <span class="word" style="left:25px;top:104px;font-size:15px">Breadsticks</span>
  <span class="word" style="left:110px;top:106px;font-size:16px">Salts</span>
  <span class="word" style="left:32px;top:118px;font-size:36px">feta</span>
  <span class="word" style="left:100px;top:128px;font-size:15px">Tzatziki</span>
  <span class="word bold" style="left:34px;top:157px;font-size:13px">Baklava</span>
  <span class="word" style="left:90px;top:155px;font-size:17px">Mastic gum</span>
  <span class="word" style="left:50px;top:175px;font-size:15px">Fruit preserves</span>
  <span class="word" style="left:113px;top:192px;font-size:13px">Spanakopita</span>
  <span class="word" style="left:30px;top:196px;font-size:25px">Halva</span>
  <span class="word bold" style="left:108px;top:208px;font-size:14px">Dried herbs</span>

  <div class="shop-mark"></div>
  <span class="shop-name">Kalo Pantry</span>
  <span class="shop-tagline">GREEK DELICATESSEN</span>

  <span class="word" style="left:340px;top:20px;font-size:40px">Beer</span>
  <span class="word bold" style="left:448px;top:19px;font-size:19px">Pita bread</span>
  <span class="word" style="left:429px;top:44px;font-size:11px">Dried herbs</span>
  <span class="word" style="left:493px;top:42px;font-size:14px">Taramasalata</span>
  <span class="word" style="left:589px;top:27px;font-size:32px">Olives</span>
  <span class="word bold" style="left:381px;top:60px;font-size:21px">Large cheese selection</span>
  <span class="word" style="left:634px;top:68px;font-size:13px">etc etc</span>
  <span class="word bold" style="left:355px;top:90px;font-size:14px">Vinegars</span>
  <span class="word" style="left:436px;top:84px;font-size:30px">Wine</span>
  <span class="word" style="left:520px;top:91px;font-size:15px">Dried fruit</span>
  <span class="word bold" style="left:601px;top:90px;font-size:18px">Dolmades</span>
  <span class="word" style="left:353px;top:110px;font-size:36px">Premium olive oils</span>
  <span class="word" style="left:574px;top:157px;font-size:17px">Jams</span>
  <span class="word" style="left:624px;top:149px;font-size:30px">Pasta</span>
  <span class="word" style="left:588px;top:182px;font-size:32px">Coffee</span>
</section>

<div class="window-label" style="top:443px">Second window (Dimensions 148cm width X 50cm height)</div>
<section class="sticker sticker-souvlaki">
  <div class="souvlaki-photo" role="img" aria-label="Photo of a souvlaki pita wrap filled with gyros meat, tomato, onion and tzatziki"></div>
  <div class="sticker-frame"></div>
  <h2 class="menu-title lead">AUTHENTIC</h2>
  <h2 class="menu-title main">GREEK SOUVLAKI</h2>
  <div class="filling-bar">GYROS | CHICKEN | VEGETERIAN</div>
  <div class="size-tag"><span>SIZE</span></div>
  <div class="size-row classic"><span class="size-name">CLASSIC</span><span class="size-price">$10.00</span></div>
  <div class="size-row jumbo"><span class="size-name">JUMBO</span><span class="size-price">$15.00</span></div>
  <svg class="clock-icon" viewBox="0 0 36 36" aria-hidden="true">
    <circle cx="18" cy="18" r="16" fill="none" stroke="var(--lime)" stroke-width="3"/>
    <circle cx="18" cy="18" r="11" fill="none" stroke="var(--lime)" stroke-width="1.5"/>
    <path d="M18 11 v7 l5 3" fill="none" stroke="var(--lime)" stroke-width="2.5" stroke-linecap="round"/>
  </svg>
  <div class="hours days">WEDNESDAY TO SUNDAY</div>
  <div class="hours time">10.30AM TO 2.30PM</div>
</section>

<div class="window-label" style="top:815px">Third window (Dimensions 220cm width X 50cm height)</div>
<section class="sticker sticker-venue">
  <div class="sticker-frame"></div>
  <div class="venue-mark"></div>
  <span class="venue-name">Marta's Table</span>
  <h2 class="venue-headline">Private Venue Available</h2>
  <p class="venue-services">Greek Cooking Lessons, Birthday Parties,<br>Corporate Lunches, Catering, Team Building and more.</p>
  <div class="venue-ask">Ask Our Friendly Staff For More Information or</div>
  <div class="venue-call">
    <span class="venue-call-label">CALL MARTA AT</span>
    <span class="venue-call-number">
      <svg class="phone-icon" viewBox="0 0 24 24" aria-hidden="true">
        <circle cx="12" cy="12" r="11" fill="var(--olive-band)"/>
        <path d="M8.5 6.5 l2 0 l1 3 l-1.5 1 a7 7 0 0 0 3.5 3.5 l1 -1.5 l3 1 l0 2 a1.5 1.5 0 0 1 -1.5 1.5 a10 10 0 0 1 -9 -9 a1.5 1.5 0 0 1 1.5 -1.5z" fill="var(--lime)"/>
      </svg>
      027359260
    </span>
  </div>
</section>

</body>
</html>
```